New Business Card Design Project

Details for my new Business Card Design Project will be added soon. Like a nice simple design

Target Market(s)

Home improvement

Industry/Entity Type

Home Improvement

Contact Information for Business Card

Roofing siding gutters additions garages decks

Requirements
Must have
• Phone 5097362418
• Email korvandpm@mailnest.net

```html
<!DOCTYPE html>
<html lang="en">
<head>
<meta charset="utf-8">
<title>Korvand Contracting – Business Card</title>
<link href="https://fonts.googleapis.com/css2?family=Bebas+Neue&display=swap" rel="stylesheet">
<style>
  :root {
    --backdrop: #ecebe8;
    --card-black: #000000;
    --card-white: #ffffff;
    --ink: #111111;
    --accent-red: #e3262f;
  }
  * { margin: 0; padding: 0; box-sizing: border-box; }
  html, body {
    width: 848px;
    height: 1200px;
    overflow: hidden;
    background: var(--backdrop);
    font-family: "Bebas Neue", "Arial Narrow", sans-serif;
  }
  .canvas {
    position: relative;
    width: 848px;
    height: 1200px;
  }
  .card {
    position: absolute;
    left: 66px;
    width: 716px;
    height: 409px;
  }
  .card-front {
    top: 168px;
    background: var(--card-black);
    color: var(--card-white);
    display: flex;
    align-items: center;
    justify-content: center;
  }
  .front-name {
    font-size: 76px;
    letter-spacing: 3px;
    line-height: 1;
  }
  .card-back {
    top: 620px;
    background: var(--card-white);
    color: var(--ink);
  }
  .back-name {
    position: absolute;
    left: 36px;
    top: 34px;
    font-size: 52px;
    letter-spacing: 2px;
    line-height: 1;
  }
  .person-name {
    position: absolute;
    left: 33px;
    top: 154px;
    font-size: 34px;
    letter-spacing: 0.5px;
    line-height: 1;
  }
  .person-title {
    position: absolute;
    left: 36px;
    top: 192px;
    font-size: 17px;
    line-height: 1;
  }
  .address {
    position: absolute;
    left: 33px;
    top: 252px;
    font-size: 19px;
    line-height: 1;
  }
  .contact {
    position: absolute;
    left: 33px;
    top: 288px;
    font-size: 19px;
    line-height: 27px;
    list-style: none;
  }
  .contact-label { color: var(--accent-red); }
  .services {
    position: absolute;
    left: 33px;
    top: 355px;
    font-size: 18px;
    line-height: 1;
    white-space: nowrap;
  }
  .services-bar {
    position: absolute;
    left: 490px;
    top: 358px;
    width: 204px;
    height: 14px;
    background: var(--ink);
  }
</style>
</head>
<body>
  <main class="canvas">
    <section class="card card-front">
      <div class="front-name">Korvand Contracting</div>
    </section>

    <section class="card card-back">
      <div class="back-name">Korvand Contracting</div>
      <h1 class="person-name">John Doe</h1>
      <p class="person-title">Director</p>
      <p class="address">Fairhollow, MA 02749</p>
      <ul class="contact">
        <li><span class="contact-label">Phone</span> 509-736-2418</li>
        <li><span class="contact-label">Email</span> korvandpm@mailnest.net</li>
      </ul>
      <p class="services">Roofing, Siding, Gutter, Additions, Decks, Handyman Services</p>
      <div class="services-bar"></div>
    </section>
  </main>
</body>
</html>
```